Business Cards
Harborline Collective
Professional
Marcus Dowd
CEO & Publisher
4870 Halberd Ave NW
Suite 415
Washington, DC 20036
Marcusd@harborlinecollective.com
www.harborlinecollective.com
see tag-line logo:
Voices that move the conversation

```html
<!DOCTYPE html>
<html lang="en">
<head>
<meta charset="utf-8">
<title>Harborline Collective Stationery</title>
<link href="https://fonts.googleapis.com/css2?family=Open+Sans:wght@400;600;700&display=swap" rel="stylesheet">
<style>
:root{
  --orange:#f27a1f;
  --blue:#2470ad;
  --ink:#444;
  --muted:#8a8a8a;
  --paper:#ffffff;
  --stage:#e9e4dc;
  --watermark:#fbeee2;
}
*{box-sizing:border-box;margin:0;padding:0}
html,body{width:1200px;height:674px;overflow:hidden}
body{background:var(--stage);font-family:"Open Sans",Arial,sans-serif;color:var(--ink);position:relative}
.piece{position:absolute;background:var(--paper);box-shadow:0 2px 6px rgba(0,0,0,.25);overflow:hidden}
.piece-label{position:absolute;font-size:7px;color:#333;font-weight:600;text-align:center;white-space:nowrap}
.brand{display:flex;align-items:center;gap:5px;white-space:nowrap}
.brand .mark{background:var(--orange);flex:none}
.brand .name{color:var(--orange);font-weight:700;letter-spacing:-.3px}
.tagline{color:var(--muted);font-size:5px;letter-spacing:.2px;white-space:nowrap}
.watermark{position:absolute;background:radial-gradient(ellipse at 50% 60%,var(--watermark),rgba(251,238,226,0) 70%)}
.bar-orange{position:absolute;height:2px;background:var(--orange)}
.corner{position:absolute;right:0;bottom:0;background:var(--blue);color:#fff;font-size:5px;padding:2px 6px 2px 14px;white-space:nowrap;clip-path:polygon(8px 0,100% 0,100% 100%,0 100%)}
.foot{position:absolute;font-size:4.5px;color:var(--muted);white-space:nowrap}

/* email signature */
.signature{left:156px;top:38px;width:364px;height:110px}
.signature .brand{position:absolute;left:18px;top:32px}
.signature .tagline{position:absolute;left:38px;top:52px}
.signature .rule{position:absolute;left:176px;top:20px;width:1px;height:66px;background:#ccc}
.signature .person{position:absolute;left:190px;top:40px;font-size:8px;color:var(--orange);font-weight:600;line-height:10px}
.signature .person small{display:block;font-size:5px;color:var(--muted);font-weight:400}
.signature .contact{position:absolute;left:262px;top:24px;font-size:5px;line-height:8px;color:var(--muted)}

/* business card */
.card-front{left:568px;top:38px;width:162px;height:70px}
.card-front .brand{position:absolute;left:8px;top:10px}
.card-front .person{position:absolute;left:8px;top:34px;font-size:6px;color:var(--orange);font-weight:600;line-height:8px}
.card-front .person small{display:block;font-size:4px;color:var(--muted);font-weight:400}
.card-front .contact{position:absolute;left:78px;top:32px;font-size:3.6px;line-height:5.4px;color:var(--muted);white-space:nowrap}

/* envelopes */
.env-10{left:746px;top:34px;width:424px;height:180px}
.env-10 .brand{position:absolute;left:16px;top:14px}
.env-10 .tagline{position:absolute;left:40px;top:34px}
.env-10 .watermark{left:110px;top:40px;width:200px;height:136px}
.env-back{left:748px;width:420px;height:84px}
.env-back .flap{position:absolute;left:0;top:0;width:100%;height:100%}
.env-back .mini{position:absolute;left:50%;transform:translateX(-50%);top:16px;display:flex;flex-direction:column;align-items:center;gap:2px}
.env-back .mini span{width:8px;height:8px;display:block}
.env-back .mini em{font-style:normal;font-size:4px;white-space:nowrap}

/* fax cover + letterhead */
.sheet{top:166px;width:334px;height:482px}
.fax{left:30px}
.letterhead{left:384px}
.sheet .brand{position:absolute;left:50%;transform:translateX(-50%);top:14px}
.sheet .tagline{position:absolute;left:0;width:100%;text-align:center;top:34px}
.sheet .watermark{left:46px;top:200px;width:240px;height:260px}
.fax-title{position:absolute;right:30px;top:56px;font-size:6px;font-weight:700}
.fax-table{position:absolute;left:30px;top:66px;width:274px;border-collapse:collapse;font-size:5px}
.fax-table td{border:1px solid #999;height:13px;padding:0 3px}
.fax-table td.key{width:28px}
.checks{position:absolute;left:30px;top:134px;display:flex;gap:14px;font-size:4.5px;white-space:nowrap}
.checks span::before{content:"";display:inline-block;width:5px;height:5px;border:1px solid #777;margin-right:3px;vertical-align:middle}
</style>
</head>
<body>

<div class="piece-label" style="left:156px;top:28px;width:364px">Email Signature</div>
<section class="piece signature">
  <div class="brand"><span class="mark" style="width:15px;height:15px"></span><span class="name" style="font-size:13px">HarborlineCollective</span></div>
  <div class="tagline">Voices that move the conversation</div>
  <div class="rule"></div>
  <div class="person">Marcus Dowd<small>CEO &amp; Publisher</small></div>
  <div class="contact">4870 Halberd Ave NW<br>Suite 415<br>Washington, DC 20036<br>p (202) 555-0147<br>f (202) 555-0192<br>Marcusd@harborlinecollective.com</div>
  <div class="bar-orange" style="left:0;right:90px;bottom:4px"></div>
  <div class="corner">www.harborlinecollective.com</div>
</section>

<div class="piece-label" style="left:568px;top:28px;width:162px">Business Card (Front)</div>
<section class="piece card-front">
  <div class="brand"><span class="mark" style="width:10px;height:10px"></span><span class="name" style="font-size:8px">HarborlineCollective</span></div>
  <div class="person">Marcus Dowd<small>CEO &amp; Publisher</small></div>
  <div class="contact">4870 Halberd Ave NW, Suite 415<br>Washington, DC 20036<br>p (202) 555-0147<br>Marcusd@harborlinecollective.com</div>
  <div class="bar-orange" style="left:0;right:60px;bottom:2px;height:1px"></div>
  <div class="corner" style="font-size:3.5px;padding:1px 4px 1px 10px">www.harborlinecollective.com</div>
</section>

<section class="piece env-10">
  <div class="brand"><span class="mark" style="width:14px;height:14px"></span><span class="name" style="font-size:11px">HarborlineCollective</span></div>
  <div class="tagline">4870 Halberd Ave NW, Suite 415, Washington, DC 20036</div>
  <div class="watermark" role="img" aria-label="Faint building dome decoration"></div>
  <div class="bar-orange" style="left:0;right:110px;bottom:5px"></div>
  <div class="corner">www.harborlinecollective.com</div>
</section>

<div class="piece-label" style="left:748px;top:244px;width:420px">Envelope Option 1 (Back)</div>
<section class="piece env-back" style="top:256px">
  <svg class="flap" viewBox="0 0 420 84" preserveAspectRatio="none"><polygon points="0,0 420,0 420,6 210,36 0,6" fill="#f4f4f4" stroke="#bbb" stroke-width=".8"/><polyline points="0,84 170,32" fill="none" stroke="#ddd"/><polyline points="420,84 250,32" fill="none" stroke="#ddd"/></svg>
  <div class="mini" style="top:10px"><span style="background:var(--orange)"></span><em style="color:var(--orange)">HarborlineCollective</em></div>
</section>

<div class="piece-label" style="left:748px;top:348px;width:420px">Envelope Option 2 (Back)</div>
<section class="piece env-back" style="top:360px">
  <svg class="flap" viewBox="0 0 420 84" preserveAspectRatio="none"><polygon points="0,0 420,0 420,8 210,40 0,8" fill="var(--orange)"/></svg>
  <div class="mini"><span style="background:#fff"></span><em style="color:#fff">HarborlineCollective</em></div>
</section>

<div class="piece-label" style="left:748px;top:452px;width:420px">Envelope Option 2 (Back)</div>
<section class="piece env-back" style="top:464px">
  <svg class="flap" viewBox="0 0 420 84" preserveAspectRatio="none"><polygon points="0,0 420,0 420,8 210,40 0,8" fill="var(--blue)"/></svg>
  <div class="mini"><span style="background:#fff"></span><em style="color:#fff">HarborlineCollective</em></div>
</section>

<div class="piece-label" style="left:30px;top:154px;width:334px">Fax Cover</div>
<section class="piece sheet fax">
  <div class="brand"><span class="mark" style="width:15px;height:15px"></span><span class="name" style="font-size:12px">HarborlineCollective</span></div>
  <div class="tagline">Voices that move the conversation</div>
  <div class="fax-title">FAX</div>
  <table class="fax-table">
    <tr><td class="key">To:</td><td></td><td class="key">From:</td><td></td></tr>
    <tr><td class="key">Fax:</td><td></td><td class="key">Pages:</td><td></td></tr>
    <tr><td class="key">Phone:</td><td></td><td class="key">Date:</td><td></td></tr>
    <tr><td class="key">Re:</td><td></td><td class="key">CC:</td><td></td></tr>
  </table>
  <div class="checks"><span>Urgent</span><span>For Review</span><span>Please Comment</span><span>Please Reply</span><span>Please Recycle</span></div>
  <div class="watermark" role="img" aria-label="Faint building dome decoration"></div>
  <div class="foot" style="left:14px;bottom:14px">4870 Halberd Ave NW, Suite 415, Washington, DC 20036 · p (202) 555-0147 · f (202) 555-0192</div>
  <div class="bar-orange" style="left:0;right:100px;bottom:5px"></div>
  <div class="corner">www.harborlinecollective.com</div>
</section>

<div class="piece-label" style="left:384px;top:154px;width:334px">Letterhead</div>
<section class="piece sheet letterhead">
  <div class="brand"><span class="mark" style="width:15px;height:15px"></span><span class="name" style="font-size:12px">HarborlineCollective</span></div>
  <div class="tagline">Voices that move the conversation</div>
  <div class="watermark" style="top:150px;height:300px" role="img" aria-label="Faint building dome decoration"></div>
  <div class="foot" style="left:14px;bottom:14px">4870 Halberd Ave NW, Suite 415, Washington, DC 20036 · p (202) 555-0147 · f (202) 555-0192</div>
  <div class="bar-orange" style="left:0;right:100px;bottom:5px"></div>
  <div class="corner">www.harborlinecollective.com</div>
</section>

</body>
</html>
```